Pelican Crest landing page design

We need a landing page designed for an ecommerce website that sales fresh US domestic shrimp from the Gulf of Mexico and ships them direct to the consumer "From Our Shore To Your Door". For the landing page, we would like customers to be able to place an order and or inquire further about our product as well as links to social media. The company logo is attached

1 page

```html
<!DOCTYPE html>
<html lang="en">
<head>
<meta charset="utf-8">
<title>Pelican Crest — From Our Shore To Your Door</title>
<link href="https://fonts.googleapis.com/css2?family=Montserrat:wght@400;500;600;700&family=Open+Sans:wght@400;600&display=swap" rel="stylesheet">
<style>
:root{
  --orange:#ec6f3c;
  --orange-dark:#d85d2c;
  --ink:#2b2b2b;
  --muted:#8a8a8a;
  --line:#e3e3e3;
  --cream:#fbf3e8;
  --slate:#9fb3c4;
  --white:#ffffff;
  --star:#ec6f3c;
}
*{box-sizing:border-box;margin:0;padding:0}
html,body{width:1200px;height:2224px;overflow:hidden;background:var(--white)}
body{font-family:"Open Sans",Arial,sans-serif;color:var(--ink);position:relative}
.page{position:relative;width:1200px;height:2224px}

/* hero */
.hero{position:absolute;left:0;top:0;width:1200px;height:712px}
.hero-photo{position:absolute;inset:0;background:linear-gradient(100deg,#3d463c 0%,#5f6a52 30%,#7a7f66 50%,#4a5244 72%,#2f352f 100%)}
.hero-shade{position:absolute;inset:0;background:linear-gradient(180deg,rgba(0,0,0,.45) 0%,rgba(0,0,0,.05) 25%,rgba(0,0,0,.1) 100%)}
.nav{position:absolute;left:112px;right:110px;top:24px;height:96px;display:flex;align-items:center}
.brand{display:flex;align-items:center;gap:14px;color:var(--white);font-family:"Montserrat",sans-serif;font-weight:700;font-size:26px;letter-spacing:2px}
.brand-dot{width:72px;height:72px;border-radius:50%;border:2px solid currentColor}
.menu{display:flex;gap:34px;margin-left:auto;font-family:"Montserrat",sans-serif;font-size:14px;font-weight:600;color:var(--white);letter-spacing:.5px}
.tools{display:flex;gap:14px;align-items:center;margin-left:40px}
.ring{width:32px;height:32px;border-radius:50%;border:1.5px solid rgba(255,255,255,.8)}
.hero-title{position:absolute;left:112px;top:302px;width:660px;font-family:"Montserrat",sans-serif;font-weight:600;font-size:54px;line-height:66px;color:var(--white);text-transform:uppercase}
.btn{display:inline-flex;align-items:center;justify-content:center;font-family:"Montserrat",sans-serif;font-weight:600;font-size:13px;letter-spacing:.5px;text-transform:uppercase;border-radius:30px}
.btn-orange{background:var(--orange);color:var(--white)}
.hero-cta{position:absolute;left:112px;top:460px;width:200px;height:44px}
.dots{position:absolute;left:560px;top:634px;display:flex;gap:10px}
.dots i{width:11px;height:11px;border-radius:50%;background:rgba(255,255,255,.6)}
.dots i:first-child{background:var(--white)}

.inquire{position:absolute;left:748px;top:232px;width:344px;height:360px;background:var(--orange);padding:26px 26px;color:var(--white)}
.inquire h2{font-family:"Montserrat",sans-serif;font-weight:600;font-size:30px;text-align:center;margin-bottom:20px}
.field{background:var(--white);height:40px;color:#9a9a9a;font-size:12px;padding:0 12px;display:flex;align-items:center;margin-bottom:12px}
.row{display:flex;gap:12px}
.row .field{flex:1}
.field.msg{height:86px;align-items:flex-start;padding-top:12px}
.send{margin-left:auto;width:110px;height:38px;background:var(--white);color:var(--orange);border-radius:20px;display:flex;align-items:center;justify-content:center;gap:10px;font-family:"Montserrat",sans-serif;font-weight:600;font-size:14px;margin-right:52px}

/* about */
.about{position:absolute;left:0;top:712px;width:1200px;height:488px;text-align:center}
.section-title{font-family:"Montserrat",sans-serif;font-weight:500;font-size:44px;color:var(--ink);letter-spacing:1px}
.about .section-title{margin-top:112px}
.rule{width:90px;height:2px;background:var(--ink);margin:18px auto 0}
.about p{width:960px;margin:40px auto 0;font-size:13px;line-height:30px;color:var(--muted)}
.about-actions{display:flex;justify-content:center;gap:30px;margin-top:42px}
.about-actions .btn{width:140px;height:40px}
.btn-slate{border:1.5px solid var(--slate);color:var(--slate)}

/* products */
.products{position:absolute;left:0;top:1200px;width:1200px;height:500px;background:var(--cream);text-align:center}
.products .section-title{margin-top:96px}
.cards{position:absolute;left:112px;top:220px;display:flex;gap:20px}
.card{width:228px;height:200px;background:var(--white);border:1px solid var(--line);text-align:left}
.card-photo{height:128px;margin:10px;border-radius:2px}
.card h3{font-family:"Montserrat",sans-serif;font-weight:600;font-size:12px;margin:6px 14px 6px;color:var(--ink)}
.stars{display:flex;gap:3px;margin-left:14px}
.card.active{background:#a8bed0}
.card.active .card-photo{background:#9cb3c6 !important;display:flex;align-items:center;justify-content:center;gap:12px}
.card.active h3{color:var(--white)}
.card-ico{width:30px;height:30px;border-radius:50%;background:rgba(255,255,255,.85)}
.arrow{position:absolute;top:308px;width:30px;height:30px;border-radius:50%;background:var(--white);border:1px solid var(--line);display:flex;align-items:center;justify-content:center}

/* footer */
.footer{position:absolute;left:0;top:1700px;width:1200px;height:524px}
.foot-brand{position:absolute;left:112px;top:120px;color:var(--ink)}
.foot-brand .brand{color:var(--ink);font-size:30px}
.foot-brand .brand-dot{width:96px;height:96px;border-color:var(--orange)}
.socials{position:absolute;left:116px;top:316px;display:flex;gap:14px}
.socials i{width:36px;height:36px;border-radius:50%;border:1.5px solid var(--orange)}
.divider{position:absolute;left:560px;top:80px;width:1px;height:320px;background:var(--line)}
.newsletter{position:absolute;left:640px;top:84px;width:440px}
.newsletter h2{font-family:"Montserrat",sans-serif;font-weight:500;font-size:34px;color:var(--ink)}
.newsletter p{font-size:12px;color:var(--muted);margin-top:14px}
.subscribe{display:flex;margin-top:24px}
.subscribe .input{width:320px;height:40px;border:1px solid var(--line);font-size:12px;color:#9a9a9a;display:flex;align-items:center;padding:0 14px}
.subscribe .btn{border-radius:0;width:120px;height:40px}
.foot-wave{position:absolute;left:600px;top:380px;width:600px;height:144px;background:linear-gradient(90deg,rgba(236,111,60,0) 0%,rgba(236,111,60,.12) 60%,rgba(236,111,60,.05) 100%)}
.legal{position:absolute;left:112px;right:110px;top:450px;display:flex;align-items:center;font-size:11px;color:var(--muted)}
.cards-pay{display:flex;gap:8px}
.cards-pay i{width:42px;height:26px;border-radius:3px;background:#d9dee6}
.legal span{margin-left:auto}
</style>
</head>
<body>
<div class="page">

<header class="hero">
  <div class="hero-photo" role="img" aria-label="Close-up photo of a hand holding fresh raw Gulf shrimp"></div>
  <div class="hero-shade"></div>
  <nav class="nav">
    <div class="brand"><span class="brand-dot"></span>PELICAN CREST</div>
    <div class="menu"><span>HOME</span><span>ABOUT US</span><span>PRODUCTS</span><span>CONTACT US</span></div>
    <div class="tools">
      <svg width="18" height="18" viewBox="0 0 18 18" fill="none" stroke="#fff" stroke-width="2"><circle cx="7.5" cy="7.5" r="5.5"/><line x1="11.5" y1="11.5" x2="16" y2="16"/></svg>
      <span class="ring"></span><span class="ring"></span>
      <svg width="22" height="20" viewBox="0 0 22 20" fill="none" stroke="#fff" stroke-width="2"><path d="M1 2h4l3 11h11l2-8H6"/><circle cx="9" cy="17" r="1.5"/><circle cx="18" cy="17" r="1.5"/></svg>
    </div>
  </nav>
  <h1 class="hero-title">From our shore to your door</h1>
  <a class="btn btn-orange hero-cta">View all products</a>
  <div class="dots"><i></i><i></i><i></i><i></i><i></i></div>

  <form class="inquire">
    <h2>INQUIRE NOW</h2>
    <div class="row"><div class="field">First Name</div><div class="field">Last Name</div></div>
    <div class="field">Phone Number</div>
    <div class="field msg">Message</div>
    <div class="send">SEND
      <svg width="18" height="18" viewBox="0 0 18 18"><circle cx="9" cy="9" r="9" fill="#ec6f3c"/><path d="M5 9h7M9 6l3 3-3 3" stroke="#fff" stroke-width="1.6" fill="none"/></svg>
    </div>
  </form>
</header>

<section class="about">
  <h2 class="section-title">ABOUT US</h2>
  <div class="rule"></div>
  <p>Sed ut perspiciatis unde omnis iste natus error sit voluptatem accusantium doloremque laudantium, totam rem aperiam, eaque ipsa quae ab illo inventore veritatis et quasi architecto beatae vitae dicta sunt explicabo. Nemo enim ipsam voluptatem quia voluptas sit aspernatur aut odit aut fugit, sed quia consequuntur magni dolores eos qui ratione.</p>
  <div class="about-actions">
    <a class="btn btn-orange">Read more</a>
    <a class="btn btn-slate">Place an order</a>
  </div>
</section>

<section class="products">
  <h2 class="section-title">PRODUCTS</h2>
  <div class="rule"></div>
  <div class="arrow" style="left:50px"><svg width="10" height="10" viewBox="0 0 10 10"><path d="M7 1L3 5l4 4" stroke="#666" stroke-width="1.6" fill="none"/></svg></div>
  <div class="arrow" style="left:1120px"><svg width="10" height="10" viewBox="0 0 10 10"><path d="M3 1l4 4-4 4" stroke="#666" stroke-width="1.6" fill="none"/></svg></div>
  <div class="cards">
    <article class="card">
      <div class="card-photo" role="img" aria-label="Photo of cooked pink shrimp" style="background:radial-gradient(circle,#f3a58a 0%,#fbe8df 70%,#fff 100%)"></div>
      <h3>SED UTPERSPICI</h3>
      <div class="stars"><svg width="70" height="12" viewBox="0 0 70 12" fill="#ec6f3c"><g id="s"><polygon points="6,0 7.8,4 12,4.4 8.8,7.2 9.8,11.6 6,9.3 2.2,11.6 3.2,7.2 0,4.4 4.2,4"/></g><use href="#s" x="14"/><use href="#s" x="28"/><use href="#s" x="42"/><use href="#s" x="56"/></svg></div>
    </article>
    <article class="card">
      <div class="card-photo" role="img" aria-label="Photo of a whole red shrimp" style="background:radial-gradient(circle,#e0603a 0%,#f8d6c8 60%,#fff 100%)"></div>
      <h3>PERSPICIATE UND</h3>
      <div class="stars"><svg width="70" height="12" viewBox="0 0 70 12" fill="#ec6f3c"><use href="#s"/><use href="#s" x="14"/><use href="#s" x="28"/><use href="#s" x="42"/><use href="#s" x="56"/></svg></div>
    </article>
    <article class="card active">
      <div class="card-photo" role="img" aria-label="Photo of a raw grey shrimp"><span class="card-ico"></span><span class="card-ico"></span></div>
      <h3>VOLUPTATEM</h3>
      <div class="stars"><svg width="70" height="12" viewBox="0 0 70 12" fill="#ec6f3c"><use href="#s"/><use href="#s" x="14"/><use href="#s" x="28"/><use href="#s" x="42"/><use href="#s" x="56"/></svg></div>
    </article>
    <article class="card">
      <div class="card-photo" role="img" aria-label="Photo of a single orange shrimp" style="background:radial-gradient(circle,#ee7a44 0%,#fbe0d0 60%,#fff 100%)"></div>
      <h3>IST VOLUPTATEM</h3>
      <div class="stars"><svg width="70" height="12" viewBox="0 0 70 12" fill="#ec6f3c"><use href="#s"/><use href="#s" x="14"/><use href="#s" x="28"/><use href="#s" x="42"/><use href="#s" x="56"/></svg></div>
    </article>
  </div>
</section>

<footer class="footer">
  <div class="foot-brand"><div class="brand"><span class="brand-dot"></span>PELICAN CREST</div></div>
  <div class="socials"><i></i><i></i><i></i><i></i></div>
  <div class="divider"></div>
  <div class="newsletter">
    <h2>SIGN UP NEWSLETTER</h2>
    <p>Sed ut perspiciatis unde omnis iste natus error</p>
    <div class="subscribe"><div class="input">Enter Email</div><a class="btn btn-orange">Sign up</a></div>
  </div>
  <div class="foot-wave" role="img" aria-label="Faint shrimp illustration decoration"></div>
  <div class="legal">
    <div class="cards-pay"><i></i><i></i><i></i><i></i><i></i></div>
    <span>© Pelican Crest 2015. All Rights Reserved &nbsp;|&nbsp; Privacy Policy</span>
  </div>
</footer>

</div>
</body>
</html>
```